Webdesign für Sicherheitsdienst
Zielgruppe
Wir sind ein Sicherheitsdienst. Schwerpunkte: Werk- und Objektschutz, Personenschutz, Veranstaltungen und Detektei. Zielgruppe: Unternehmer, Behörden und Privatpersonen
Aufgabenstellung
Farben: Blau und weiß (wie das Logo), seriöses, edles Auftreten, wechselnde bzw. laufende Bilder einbauen, Beispiel: https://www.halvoro-tage.events/.
Hauptaugenmerk liegt für uns auf eine ordentliche, aufgeräumte, seriöse Homepage, um Kunden und Mitarbeiter zu gewinnen

```html
<!DOCTYPE html>
<html lang="de">
<head>
<meta charset="utf-8">
<title>Kaltwacht Sicherheitsdienst – Webdesign</title>
<link href="https://fonts.googleapis.com/css2?family=Mulish:wght@400;600;700&family=Arimo:wght@400;700&display=swap" rel="stylesheet">
<style>
:root{
  --board:#354b6d;
  --navy:#21407a;
  --blue:#2b5d9b;
  --graphite:#4a4a4a;
  --paper:#f5f6f8;
  --white:#ffffff;
  --text:#5b5f66;
  --line:#d7dbe2;
}
*{box-sizing:border-box;margin:0;padding:0}
html,body{width:1071px;height:1200px;overflow:hidden;background:var(--board)}
body{font-family:'Arimo',Arial,sans-serif;color:var(--text)}
.board{position:relative;width:1071px;height:1200px;overflow:hidden;background:var(--board)}

/* ---------- shared page frame ---------- */
.page{position:absolute;transform-origin:0 0;background:var(--white);overflow:hidden}
.photo{position:absolute}
.nav{position:absolute;display:flex;align-items:center;font-family:'Mulish',sans-serif}
.logo{display:flex;align-items:center;gap:.4em;font-weight:700;letter-spacing:.05em}
.logo i{display:block;width:1.6em;height:1.6em;background:var(--white)}
.nav-links{margin-left:auto;display:flex;align-items:center;gap:1.9em}
.nav-links .cta{background:var(--blue);color:var(--white);padding:.25em 1.6em}
.nav--light{color:var(--white)}
.nav--dark{color:var(--graphite)}
.nav--dark .logo{color:var(--navy)}
.nav--dark .logo i{background:var(--navy)}
.nav-links .is-active{border-bottom:.12em solid var(--navy)}

/* footer (em-based, scales with font-size) */
.ft{position:absolute;left:0;right:0;bottom:0;background:var(--blue);color:var(--white);line-height:1.35}
.ft-addr{position:absolute;left:10.2em;top:3.6em;width:30em}
.ft-addr p{margin-bottom:.6em}
.ft-links{position:absolute;left:40em;top:3.6em;width:18em;text-align:center}
.ft-links p{margin-bottom:.9em}
.social{display:flex;justify-content:center;gap:1.6em}
.social i{display:block;width:1em;height:1em;border-radius:50%;background:var(--white)}
.ft-copy{position:absolute;right:7.6em;bottom:1.4em;font-size:.75em}

/* ---------- home page (542 x 1007 units) ---------- */
.home{width:542px;height:1007px}
.home .hero{left:0;top:0;width:542px;height:305px}
.home .nav{top:10px;left:20px;right:30px;font-size:6.5px}
.home .side-social{position:absolute;left:33px;top:52px;display:flex;flex-direction:column;gap:8px}
.home .side-social i{display:block;width:5px;height:5px;border-radius:50%;background:var(--white)}
.hero-arrow{position:absolute;top:140px;font-size:22px;color:rgba(255,255,255,.35);font-family:'Mulish',sans-serif}
.hero-dots{position:absolute;top:259px;left:0;right:0;display:flex;justify-content:center;gap:3px}
.hero-dots i{width:3px;height:3px;border-radius:50%;background:var(--white)}
.hero-copy{position:absolute;color:var(--white);font-family:'Mulish',sans-serif}
.hero-copy h1{font-weight:600}
.hero-copy p{font-size:7px;line-height:1.45;margin-top:10px}
.tabs{position:absolute;left:75px;top:283px;width:392px;height:17px;background:var(--white);display:flex;font-size:7px;color:var(--graphite);font-family:'Mulish',sans-serif}
.tabs span{flex:1;text-align:center;line-height:17px}
.tiles{position:absolute;left:75px;top:300px;width:392px;height:81px;display:flex}
.tile{position:relative;flex:1}
.tile .tile-arrow{position:absolute;right:3px;bottom:3px;width:10px;height:10px;background:var(--white);color:var(--graphite);font-size:9px;line-height:9px;text-align:center}
.about-photo{left:75px;top:467px;width:159px;height:105px;box-shadow:0 6px 14px rgba(0,0,0,.18)}
.about h2{position:absolute;left:252px;top:470px;font-family:'Mulish',sans-serif;font-weight:400;font-size:15px;color:var(--navy)}
.about p{position:absolute;left:252px;top:507px;width:215px;font-size:6.3px;line-height:1.38}
.about .more{position:absolute;left:454px;top:551px;font-size:17px;color:var(--navy);font-family:'Mulish',sans-serif}
.help h2{position:absolute;top:657px;left:0;right:0;text-align:center;font-family:'Mulish',sans-serif;font-weight:400;font-size:15.5px;color:var(--navy)}
.help p{position:absolute;top:700px;left:71px;width:400px;text-align:center;font-size:7.3px;line-height:1.7}
.btn{position:absolute;background:var(--navy);color:var(--white);text-align:center;font-family:'Mulish',sans-serif}
.help .btn{left:166px;top:786px;width:210px;height:26px;line-height:26px;font-size:8.5px}
.home .ft{height:114px;font-size:5.4px}

/* photo tones */
.ph-castle{background:linear-gradient(180deg,#75828e 0%,#5d6a66 32%,#34412f 62%,#1f2719 100%)}
.ph-city{background:radial-gradient(circle at 30% 35%,rgba(214,168,92,.55),transparent 35%),radial-gradient(circle at 70% 70%,rgba(210,150,70,.45),transparent 40%),radial-gradient(circle at 62% 90%,rgba(60,190,90,.35),transparent 25%),linear-gradient(170deg,#454440,#1e2632 55%,#1b2a24)}
.ph-guard{background:radial-gradient(circle at 20% 40%,rgba(150,110,70,.55),transparent 40%),linear-gradient(180deg,#8fb1cc 0%,#6a87a0 35%,#2d4262 70%,#1b2a45 100%)}
.ph-tile1{background:linear-gradient(160deg,#9ba09c,#3b3c38 55%,#1d1e1c)}
.ph-tile2{background:linear-gradient(150deg,#eef0f1,#8c949c 45%,#2a2d33)}
.ph-tile3{background:linear-gradient(150deg,#b7bbc0,#7d848d)}
.ph-tile4{background:linear-gradient(150deg,#f1f3f5,#c9d1da 55%,#5d7594)}
.ph-ceo{background:linear-gradient(90deg,#e8eaec,#b8bdc2 45%,#3a3f48 55%,#d6d9dc)}
.ph-ceo-wide{background:radial-gradient(ellipse at 50% 60%,#5a5f66 0,#8d9298 22%,transparent 40%),linear-gradient(90deg,#c9ccd0,#eef0f2 40%,#e5e7e9 60%,#b7bbc0)}

/* ---------- small pages (366-unit width) ---------- */
.small .nav{top:5px;left:14px;right:14px;font-size:4.4px}
.small .ft{font-size:3.65px}
.sect-title{position:absolute;font-family:'Mulish',sans-serif;font-weight:700;color:var(--navy)}
.copy{position:absolute;font-size:3.3px;line-height:1.5}
.copy p{margin-bottom:4px}

/* Leistungen */
.services{width:366px;height:315px}
.panels{position:absolute;left:0;top:0;width:366px;height:125px;display:flex}
.panel{position:relative;flex:1}
.panel span{position:absolute;left:7px;bottom:8px;color:var(--white);font-size:5.5px;font-family:'Mulish',sans-serif}
.panel b{position:absolute;right:2px;bottom:3px;width:9px;height:9px;background:rgba(255,255,255,.85);color:var(--graphite);font-size:8px;line-height:8px;text-align:center;font-weight:400}
.services .ft{height:78px}

/* News */
.news{width:366px;height:300px}
.cards{position:absolute;left:14px;top:68px;width:338px;display:flex;gap:27px}
.card{position:relative;width:95px;height:105px}
.card .pic{height:57px}
.card h3{font-size:4.3px;color:var(--graphite);margin-top:4px;line-height:1.3;font-family:'Mulish',sans-serif}
.card p{font-size:2.8px;margin-top:3px;line-height:1.4;padding-right:11px}
.card .go{position:absolute;right:0;bottom:0;width:9px;height:9px;background:var(--navy);color:var(--white);font-size:8px;line-height:8px;text-align:center}
.more-link{position:absolute;top:193px;left:0;right:0;text-align:center;font-size:4px;color:var(--navy);font-family:'Mulish',sans-serif}
.news .ft{height:79px}
.ph-fire{background:radial-gradient(circle at 50% 40%,#d23a55,#6a0e22 45%,#1a0a10)}
.ph-poster{background:linear-gradient(180deg,#e4d4b4,#e86a3a 45%,#f2e8d8)}
.ph-dog{background:linear-gradient(90deg,#5a4a36,#2c2820 50%,#c8a23a)}

/* Unternehmen */
.company{width:366px;height:695px}
.company .quote{position:absolute;top:100px;left:0;right:0;text-align:center;color:var(--white);font-family:'Mulish',sans-serif;font-size:10.5px}
.values{position:absolute;left:100px;top:256px;width:230px}
.value{display:flex;gap:0;margin-bottom:18px}
.value h4{width:93px;font-family:'Mulish',sans-serif;font-weight:600;font-size:4.4px;color:var(--navy);padding-top:10px}
.value p{width:122px;font-size:2.8px;line-height:1.45}
.company .ft{height:78px}

/* Karriere */
.jobs{width:366px;height:670px;background:var(--paper)}
.jobs .topbar{position:absolute;left:0;top:0;right:0;height:26px;background:var(--white)}
.job{position:absolute;left:14px;width:338px;background:var(--white);border:.5px solid var(--line)}
.job h3{position:absolute;left:9px;top:6px;font-family:'Mulish',sans-serif;font-size:4.5px;color:var(--navy);font-weight:700}
.job h3 small{font-size:2.3px;font-weight:400}
.job .ref{position:absolute;right:9px;top:7px;font-size:3px;color:#a5abb4}
.job-cols{position:absolute;left:9px;top:20px;display:flex;gap:26px}
.job-cols div{width:90px}
.job-cols h4{font-weight:400;font-size:4px;color:var(--navy);margin-bottom:4px;font-family:'Mulish',sans-serif}
.job-cols p{font-size:2.4px;line-height:1.35}
.job .apply{left:9px;width:315px;height:10px;line-height:10px;font-size:2.8px}
.form{position:absolute;left:43px;top:98px;width:242px;font-size:2.3px;color:var(--graphite)}
.field{position:absolute}
.field span{display:block;font-weight:700;margin-bottom:1.5px}
.field i{display:block;height:5px;border:.4px solid #bfc5ce;background:var(--white)}
.upload{position:absolute;text-align:center;width:26px}
.upload span{display:block;font-weight:700;margin-bottom:3px}
.upload i{display:block;margin:0 auto 2px;width:5px;height:6px;border:.5px solid var(--graphite)}
.form textarea{position:absolute;left:0;top:137px;width:242px;height:60px;border:.4px solid #bfc5ce;background:var(--white);font:2.4px 'Arimo',sans-serif;color:#8a9099;padding:2px;resize:none}
.jobs .ft{height:78px}

/* ---------- colour swatches ---------- */
.swatches{position:absolute;width:132px;height:32px;border-radius:16px;background:var(--paper);display:flex;align-items:center;gap:4px;padding:0 2px}
.swatches i{display:block;width:29px;height:29px;border-radius:50%}
.sw-graphite{background:var(--graphite)}
.sw-blue{background:var(--blue)}
.sw-navy{background:var(--navy)}
.sw-paper{background:var(--paper);border:.5px solid #e3e6ea}
</style>
</head>
<body>
<main class="board">

<!-- ===== colour palettes ===== -->
<div class="swatches" style="left:876px;top:16px"><i class="sw-paper"></i><i class="sw-navy"></i><i class="sw-blue"></i><i class="sw-graphite"></i></div>
<div class="swatches" style="left:62px;top:456px"><i class="sw-graphite"></i><i class="sw-blue"></i><i class="sw-navy"></i><i class="sw-paper"></i></div>

<!-- ===== Startseite (small) ===== -->
<section class="page home" style="left:61px;top:32px;transform:scale(.397)">
  <div class="photo hero ph-castle" role="img" aria-label="Sicherheitsteam in dunkler Kleidung vor einem Schloss"></div>
  <nav class="nav nav--light"><div class="logo"><i></i><span>KALTWACHT</span></div><div class="nav-links"><span>Home</span><span>Leistungen</span><span>News</span><span>Unternehmen</span><span>Karriere</span><span class="cta">Kontakt</span></div></nav>
  <div class="side-social"><i></i><i></i></div>
  <div class="hero-copy" style="left:261px;top:108px;width:230px"><h1 style="font-size:11.5px">Diskretion wird hier groß geschrieben</h1><p>Unser Personal verfügt über die Ausbildung gemäß §34a der Gewerbeordnung (GewO) und handelt im Sinne eines Dienstleisters. Kundenfreundlichkeit und Konfliktlösungen stehen im Vordergrund.</p></div>
  <div class="hero-dots"><i></i><i></i><i></i></div>
  <div class="tabs"><span>Sicherheitsdienst</span><span>Detektei</span><span>Service</span><span>Schulungen</span></div>
  <div class="tiles">
    <div class="tile ph-tile1" role="img" aria-label="Sicherheitsmitarbeiter mit Helm"><span class="tile-arrow">›</span></div>
    <div class="tile ph-tile2" role="img" aria-label="Detektiv mit Fernglas im Auto"><span class="tile-arrow">›</span></div>
    <div class="tile ph-tile3" role="img" aria-label="Servicemitarbeiterin am Empfang"><span class="tile-arrow">›</span></div>
    <div class="tile ph-tile4" role="img" aria-label="Schulung im Besprechungsraum"><span class="tile-arrow">›</span></div>
  </div>
  <div class="photo about-photo ph-ceo" role="img" aria-label="Geschäftsführer im Anzug"></div>
  <div class="about"><h2>Über uns</h2><p>Wir sind ein inhabergeführtes Unternehmen mit Verantwortungsbewusstsein für Sicherheit und Service. Durch unseren eigenen hohen Qualitätsanspruch und unsere Flexibilität haben wir seit Firmengründung ein kontinuierliches Wachstum zu verzeichnen.</p><span class="more">›</span></div>
  <div class="help"><h2>Wie können wir Ihnen helfen…</h2><p>Unsere Leistungen sind vielfältig. Daher haben wir unsere Fachgebiete für Sie einzeln aufgegliedert.<br>Erfahren Sie mehr über uns und wählen Sie nun Ihre Wunschleistung aus.<br>Gerne beraten wir Sie vorab persönlich und helfen Ihnen eine maßgeschneiderte Dienstleistung für Sie zu finden.</p><div class="btn">Kontaktieren Sie uns</div></div>
  <footer class="ft"><div class="ft-addr"><p>Anschrift:<br>Kaltwacht Sicherheitsdienst Nürnberg e. K.<br>Lindenhofstr. 18<br>90471 Nürnberg</p><p>E-Mail:<br>info@kaltwacht-sicherheit.de</p><p>Telefon:<br>0800 / 555 010 0 (kostenfrei, 24h)<br>0911 / 555 012 30</p></div><div class="ft-links"><p>Impressum</p><p>Datenschutz</p><p>Anfahrt</p><p>Folgen Sie uns auf</p><div class="social"><i></i><i></i></div></div><p class="ft-copy">© Copyright 2020 Kaltwacht Sicherheitsdienst Nürnberg</p></footer>
</section>

<!-- ===== Leistungen ===== -->
<section class="page small services" style="left:314px;top:68px;transform:scale(.5885)">
  <div class="panels">
    <div class="panel ph-tile1" role="img" aria-label="Sicherheitsmitarbeiter mit Helm"><span>Sicherheitsdienst</span><b>›</b></div>
    <div class="panel ph-tile2" role="img" aria-label="Detektiv mit Fernglas"><span>Detektei</span><b>›</b></div>
    <div class="panel ph-tile3" role="img" aria-label="Servicemitarbeiterin"><span>Service</span><b>›</b></div>
    <div class="panel ph-tile4" role="img" aria-label="Schulung im Büro"><span>Schulungen</span><b>›</b></div>
  </div>
  <nav class="nav nav--light"><div class="logo"><i></i><span>KALTWACHT</span></div><div class="nav-links"><span>Home</span><span>Leistungen</span><span>News</span><span>Unternehmen</span><span>Karriere</span><span class="cta">Kontakt</span></div></nav>
  <h2 class="sect-title" style="left:23px;top:150px;font-size:7.5px">Leistungen</h2>
  <div class="copy" style="left:23px;top:172px;width:320px"><p>Unsere Leistungen sind vielfältig. Daher haben wir unsere Fachgebiete für Sie einzeln aufgegliedert.</p><p>Erfahren Sie mehr über uns und wählen Sie nun Ihre Wunschleistung aus.</p><p>Anfragen zu Kunden und Stundensätzen erhalten Sie über das Anfrageformular. Gerne beraten wir Sie vorab persönlich und helfen Ihnen, eine maßgeschneiderte Dienstleistung für Sie zu finden. Rufen Sie uns an. Wir sind 24 Stunden täglich für Sie unter 0911 / 555 012 30 erreichbar.</p></div>
  <footer class="ft"><div class="ft-addr"><p>Anschrift:<br>Kaltwacht Sicherheitsdienst Nürnberg e. K.<br>Lindenhofstr. 18<br>90471 Nürnberg</p><p>E-Mail:<br>info@kaltwacht-sicherheit.de</p><p>Telefon:<br>0800 / 555 010 0 (kostenfrei, 24h)<br>0911 / 555 012 30</p></div><div class="ft-links"><p>Impressum</p><p>Datenschutz</p><p>Anfahrt</p><p>Folgen Sie uns auf</p><div class="social"><i></i><i></i></div></div><p class="ft-copy">© Copyright 2020 Kaltwacht Sicherheitsdienst Nürnberg</p></footer>
</section>

<!-- ===== News ===== -->
<section class="page small news" style="left:314px;top:289px;transform:scale(.5885)">
  <nav class="nav nav--dark"><div class="logo"><i></i><span>KALTWACHT</span></div><div class="nav-links"><span>Home</span><span>Leistungen</span><span class="is-active">News</span><span>Unternehmen</span><span>Karriere</span><span class="cta">Kontakt</span></div></nav>
  <h2 class="sect-title" style="left:14px;top:43px;font-size:8.5px">Aktuelle News</h2>
  <div class="cards">
    <article class="card"><div class="pic ph-fire" role="img" aria-label="Feuerwerk am Nachthimmel"></div><h3>Vor lauter Freude haben wir erstmal ein Feuerwerk gezündet</h3><p>Seit kurzem dürfen wir die wunderbare Veranstaltungsreihe im Kulturpark sicher begleiten.</p><span class="go">›</span></article>
    <article class="card"><div class="pic ph-poster" role="img" aria-label="Plakat einer Sommerveranstaltung"></div><h3>… und wir sind mit dabei!</h3><p>SOMMERKLANG AM MARKT 2020<br>Endlich wieder was los in der Stadt</p><span class="go">›</span></article>
    <article class="card"><div class="pic ph-dog" role="img" aria-label="Sicherheitskraft mit Diensthund"></div><h3>Partnerfirma Nordtor Security Solution</h3><p>Eine Bewachung mit Hunden ist immer eine Herausforderung. Das Team hat sich mit uns zusammengeschlossen.</p><span class="go">›</span></article>
  </div>
  <p class="more-link">Mehr …</p>
  <footer class="ft"><div class="ft-addr"><p>Anschrift:<br>Kaltwacht Sicherheitsdienst Nürnberg e. K.<br>Lindenhofstr. 18<br>90471 Nürnberg</p><p>E-Mail:<br>info@kaltwacht-sicherheit.de</p><p>Telefon:<br>0800 / 555 010 0 (kostenfrei, 24h)<br>0911 / 555 012 30</p></div><div class="ft-links"><p>Impressum</p><p>Datenschutz</p><p>Anfahrt</p><p>Folgen Sie uns auf</p><div class="social"><i></i><i></i></div></div><p class="ft-copy">© Copyright 2020 Kaltwacht Sicherheitsdienst Nürnberg</p></footer>
</section>

<!-- ===== Unternehmen ===== -->
<section class="page small company" style="left:554px;top:32px;transform:scale(.5885)">
  <div class="photo ph-ceo-wide" style="left:0;top:0;width:366px;height:205px" role="img" aria-label="Geschäftsführer im Anzug in heller Architektur"></div>
  <nav class="nav nav--light"><div class="logo"><i></i><span>KALTWACHT</span></div><div class="nav-links"><span>Home</span><span>Leistungen</span><span>News</span><span>Unternehmen</span><span>Karriere</span><span class="cta">Kontakt</span></div></nav>
  <p class="quote">„Diskretion wird hier groß geschrieben“</p>
  <h2 class="sect-title" style="left:23px;top:226px;font-size:6px">Firmenphilosophie</h2>
  <div class="values">
    <div class="value"><h4>Problemlöser</h4><p>Nur motiviertes und eingespieltes Personal gewährt einen möglichst reibungslosen Ablauf. Unsere Führungskräfte sind im Umgang mit Menschen ausgebildet und stehen Ihnen auch als Ansprechpartner zur Lösungsfindung bei Problemen zur Seite.</p></div>
    <div class="value"><h4>Teamwork</h4><p>Um den Kunden zufrieden zu stellen, bedarf es eines harmonischen Zusammenwirkens von Einsatzleitung und Mitarbeitern, die im Sinne des Kunden handeln. Aus diesem Grund sehen wir unser Team als das wichtigste Element jedes Einsatzes.</p></div>
    <div class="value"><h4>Geschultes<br>Personal</h4><p>Unsere Mitarbeiter sind nach §34a der Gewerbeordnung geschult und ausgebildet, was die Grundvoraussetzung für ein erfolgreiches Arbeiten im Sicherheitsbereich darstellt. Darüber hinaus durchlaufen sie intensive Gesprächsschulungen, um Ihrem hohen Anspruch gerecht zu werden. Der Mitarbeiter steht somit im Mittelpunkt unserer Firma.</p></div>
    <div class="value"><h4>Engagiertes<br>Team</h4><p>Ziel ist es, dass sich Mitarbeiter in ihrem Arbeitsumfeld engagiert einsetzen und mit dem Leitbild der Firma identifizieren. Gleichzeitig wollen wir dadurch den Kunden zufriedenstellen und seinen Wünschen gerecht werden.</p></div>
  </div>
  <h2 class="sect-title" style="left:21px;top:518px;font-size:6px">Referenzen</h2>
  <div class="copy" style="left:21px;top:537px;width:330px;font-size:2.8px"><p>Wir bitten um Verständnis, dass wir aus Diskretion und datenschutzrechtlichen Gründen unsere Kunden nicht öffentlich nennen möchten. Das uns entgegengebrachte Vertrauen wahren wir nicht als Selbstverständlichkeit.</p><p>Gerne erhalten Sie Referenzen in einem persönlichen Gespräch, soweit die jeweiligen Auftraggeber vorher ihre Genehmigung erteilt haben.</p><p>Eine Verschwiegenheitsverpflichtung über Informationen aus unserer Tätigkeit ist für uns selbstverständlich.</p></div>
  <footer class="ft"><div class="ft-addr"><p>Anschrift:<br>Kaltwacht Sicherheitsdienst Nürnberg e. K.<br>Lindenhofstr. 18<br>90471 Nürnberg</p><p>E-Mail:<br>info@kaltwacht-sicherheit.de</p><p>Telefon:<br>0800 / 555 010 0 (kostenfrei, 24h)<br>0911 / 555 012 30</p></div><div class="ft-links"><p>Impressum</p><p>Datenschutz</p><p>Anfahrt</p><p>Folgen Sie uns auf</p><div class="social"><i></i><i></i></div></div><p class="ft-copy">© Copyright 2020 Kaltwacht Sicherheitsdienst Nürnberg</p></footer>
</section>

<!-- ===== Karriere ===== -->
<section class="page small jobs" style="left:794px;top:68px;transform:scale(.5885)">
  <div class="topbar"></div>
  <nav class="nav nav--dark"><div class="logo"><i></i><span>KALTWACHT</span></div><div class="nav-links"><span>Home</span><span>Leistungen</span><span>News</span><span>Unternehmen</span><span class="is-active">Karriere</span><span class="cta">Kontakt</span></div></nav>
  <h2 class="sect-title" style="left:14px;top:34px;font-size:6.5px">Stellenangebote</h2>
  <p class="copy" style="left:14px;top:43px;font-size:2.8px">Sie wollen bei uns durchstarten? Dann bewerben Sie sich auf unsere offenen Stellen. Wir freuen uns auf Ihre aussagekräftige Bewerbung!</p>

  <article class="job" style="top:62px;height:90px">
    <h3>Werkschutz (m/w/d) <small>• Nürnberg</small></h3><span class="ref">Stelle 0001</span>
    <div class="job-cols"><div><h4>Ihre Aufgaben</h4><p>Bewachungstätigkeiten<br>Werkschutz<br>Zugangskontrolle<br>Streifendienst</p></div><div><h4>Ihre Voraussetzungen</h4><p>sympathisches Auftreten<br>Durchsetzungsfähigkeit<br>Teamplayer<br>Sachkundeprüfung §34a<br>Unterrichtung oder höher</p></div><div><h4>Konditionen</h4><p>gemäß Tarifvertrag Bewachungsgewerbe</p></div></div>
    <div class="btn apply" style="top:72px">›&nbsp;&nbsp; Jetzt bewerben</div>
  </article>

  <article class="job" style="top:160px;height:332px">
    <h3>Aushilfe (m/w/d) <small>• Nürnberg</small></h3><span class="ref">Stelle 0002</span>
    <div class="job-cols"><div><h4>Ihre Aufgaben</h4><p>Bewachungstätigkeiten<br>Werkschutz<br>Zugangskontrolle<br>Streifendienst</p></div><div><h4>Ihre Voraussetzungen</h4><p>sympathisches Auftreten<br>Durchsetzungsfähigkeit<br>Teamplayer<br>Sachkundeprüfung §34a<br>Unterrichtung oder höher</p></div><div><h4>Konditionen</h4><p>gemäß Tarifvertrag Bewachungsgewerbe</p></div></div>
    <div class="btn apply" style="top:72px">›&nbsp;&nbsp; Jetzt bewerben</div>
    <div class="form">
      <div class="field" style="left:0;top:0;width:54px"><span>Anrede</span><i></i></div>
      <div class="field" style="left:58px;top:0;width:54px"><span>Arbeitsbeginn</span><i></i></div>
      <div class="field" style="left:0;top:20px;width:113px"><span>Name</span><i></i></div>
      <div class="field" style="left:128px;top:20px;width:113px"><span>Vorname</span><i></i></div>
      <div class="field" style="left:0;top:42px;width:113px"><span>Ort</span><i></i></div>
      <div class="field" style="left:128px;top:42px;width:113px"><span>PLZ</span><i></i></div>
      <div class="field" style="left:0;top:64px;width:113px"><span>Telefon</span><i></i></div>
      <div class="field" style="left:128px;top:64px;width:113px"><span>Email</span><i></i></div>
      <div class="upload" style="left:-6px;top:92px"><span>Lebenslauf</span><i></i>Datei wählen</div>
      <div class="upload" style="left:51px;top:92px"><span>Qualifikationen</span><i></i>Datei wählen</div>
      <div class="upload" style="left:103px;top:92px"><span>Foto</span><i></i>Datei wählen</div>
      <div class="upload" style="left:155px;top:92px"><span>Anschreiben</span><i></i>Datei wählen</div>
      <div class="upload" style="left:208px;top:92px"><span>Sonstiges</span><i></i>Datei wählen</div>
      <div class="field" style="left:0;top:127px;width:60px"><span>Bemerkung</span></div>
      <textarea aria-label="Bemerkung">Was wollen wir noch wissen?</textarea>
      <div class="btn" style="left:188px;top:207px;width:54px;height:10px;line-height:10px;font-size:2.8px">Abschicken</div>
    </div>
  </article>

  <article class="job" style="top:498px;height:88px">
    <h3>Doorman (m/w/d) <small>• Nürnberg</small></h3><span class="ref">Stelle 0003</span>
    <div class="job-cols"><div><h4>Ihre Aufgaben</h4><p>Bewachungstätigkeiten<br>Werkschutz<br>Zugangskontrolle<br>Streifendienst</p></div><div><h4>Ihre Voraussetzungen</h4><p>sympathisches Auftreten<br>Durchsetzungsfähigkeit<br>Teamplayer<br>Sachkundeprüfung §34a<br>Unterrichtung oder höher</p></div><div><h4>Konditionen</h4><p>gemäß Tarifvertrag Bewachungsgewerbe</p></div></div>
    <div class="btn apply" style="top:70px">›&nbsp;&nbsp; Jetzt bewerben</div>
  </article>
  <footer class="ft"><div class="ft-addr"><p>Anschrift:<br>Kaltwacht Sicherheitsdienst Nürnberg e. K.<br>Lindenhofstr. 18<br>90471 Nürnberg</p><p>E-Mail:<br>info@kaltwacht-sicherheit.de</p><p>Telefon:<br>0800 / 555 010 0 (kostenfrei, 24h)<br>0911 / 555 012 30</p></div><div class="ft-links"><p>Impressum</p><p>Datenschutz</p><p>Anfahrt</p><p>Folgen Sie uns auf</p><div class="social"><i></i><i></i></div></div><p class="ft-copy">© Copyright 2020 Kaltwacht Sicherheitsdienst Nürnberg</p></footer>
</section>

<!-- ===== Startseite, Slider-Varianten ===== -->
<section class="page home" style="left:28px;top:552px;transform:scale(.5885)">
  <div class="photo hero ph-city" role="img" aria-label="Nächtliche Skyline von Abu Dhabi aus der Vogelperspektive"></div>
  <nav class="nav nav--light"><div class="logo"><i></i><span>KALTWACHT</span></div><div class="nav-links"><span>Home</span><span>Leistungen</span><span>News</span><span>Unternehmen</span><span>Karriere</span><span class="cta">Kontakt</span></div></nav>
  <div class="side-social"><i></i><i></i></div>
  <span class="hero-arrow" style="left:40px">‹</span><span class="hero-arrow" style="right:40px">›</span>
  <div class="hero-copy" style="left:335px;top:140px"><h1 style="font-size:17px">… in Abu Dhabi</h1></div>
  <div class="hero-dots"><i></i><i></i><i></i></div>
  <div class="tabs"><span>Sicherheitsdienst</span><span>Detektei</span><span>Service</span><span>Schulungen</span></div>
  <div class="tiles">
    <div class="tile ph-tile1" role="img" aria-label="Sicherheitsmitarbeiter mit Helm"><span class="tile-arrow">›</span></div>
    <div class="tile ph-tile2" role="img" aria-label="Detektiv mit Fernglas im Auto"><span class="tile-arrow">›</span></div>
    <div class="tile ph-tile3" role="img" aria-label="Servicemitarbeiterin am Empfang"><span class="tile-arrow">›</span></div>
    <div class="tile ph-tile4" role="img" aria-label="Schulung im Besprechungsraum"><span class="tile-arrow">›</span></div>
  </div>
  <div class="photo about-photo ph-ceo" role="img" aria-label="Geschäftsführer im Anzug"></div>
  <div class="about"><h2>Über uns</h2><p>Wir sind ein inhabergeführtes Unternehmen mit Verantwortungsbewusstsein für Sicherheit und Service. Durch unseren eigenen hohen Qualitätsanspruch und unsere Flexibilität haben wir seit Firmengründung ein kontinuierliches Wachstum zu verzeichnen.</p><span class="more">›</span></div>
  <div class="help"><h2>Wie können wir Ihnen helfen…</h2><p>Unsere Leistungen sind vielfältig. Daher haben wir unsere Fachgebiete für Sie einzeln aufgegliedert.<br>Erfahren Sie mehr über uns und wählen Sie nun Ihre Wunschleistung aus.<br>Gerne beraten wir Sie vorab persönlich und helfen Ihnen eine maßgeschneiderte Dienstleistung für Sie zu finden.</p><div class="btn">Kontaktieren Sie uns</div></div>
  <footer class="ft"><div class="ft-addr"><p>Anschrift:<br>Kaltwacht Sicherheitsdienst Nürnberg e. K.<br>Lindenhofstr. 18<br>90471 Nürnberg</p><p>E-Mail:<br>info@kaltwacht-sicherheit.de</p><p>Telefon:<br>0800 / 555 010 0 (kostenfrei, 24h)<br>0911 / 555 012 30</p></div><div class="ft-links"><p>Impressum</p><p>Datenschutz</p><p>Anfahrt</p><p>Folgen Sie uns auf</p><div class="social"><i></i><i></i></div></div><p class="ft-copy">© Copyright 2020 Kaltwacht Sicherheitsdienst Nürnberg</p></footer>
</section>

<section class="page home" style="left:376px;top:552px;transform:scale(.5885)">
  <div class="photo hero ph-castle" role="img" aria-label="Sicherheitsteam in dunkler Kleidung vor einem Schloss"></div>
  <nav class="nav nav--light"><div class="logo"><i></i><span>KALTWACHT</span></div><div class="nav-links"><span>Home</span><span>Leistungen</span><span>News</span><span>Unternehmen</span><span>Karriere</span><span class="cta">Kontakt</span></div></nav>
  <div class="side-social"><i></i><i></i></div>
  <span class="hero-arrow" style="left:40px">‹</span><span class="hero-arrow" style="right:40px">›</span>
  <div class="hero-copy" style="left:261px;top:108px;width:230px"><h1 style="font-size:11.5px">Diskretion wird hier groß geschrieben</h1><p>Unser Personal verfügt über die Ausbildung gemäß §34a der Gewerbeordnung (GewO) und handelt im Sinne eines Dienstleisters. Kundenfreundlichkeit und Konfliktlösungen stehen im Vordergrund.</p></div>
  <div class="hero-dots"><i></i><i></i><i></i></div>
  <div class="tabs"><span>Sicherheitsdienst</span><span>Detektei</span><span>Service</span><span>Schulungen</span></div>
  <div class="tiles">
    <div class="tile ph-tile1" role="img" aria-label="Sicherheitsmitarbeiter mit Helm"><span class="tile-arrow">›</span></div>
    <div class="tile ph-tile2" role="img" aria-label="Detektiv mit Fernglas im Auto"><span class="tile-arrow">›</span></div>
    <div class="tile ph-tile3" role="img" aria-label="Servicemitarbeiterin am Empfang"><span class="tile-arrow">›</span></div>
    <div class="tile ph-tile4" role="img" aria-label="Schulung im Besprechungsraum"><span class="tile-arrow">›</span></div>
  </div>
  <div class="photo about-photo ph-ceo" role="img" aria-label="Geschäftsführer im Anzug"></div>
  <div class="about"><h2>Über uns</h2><p>Wir sind ein inhabergeführtes Unternehmen mit Verantwortungsbewusstsein für Sicherheit und Service. Durch unseren eigenen hohen Qualitätsanspruch und unsere Flexibilität haben wir seit Firmengründung ein kontinuierliches Wachstum zu verzeichnen.</p><span class="more">›</span></div>
  <div class="help"><h2>Wie können wir Ihnen helfen…</h2><p>Unsere Leistungen sind vielfältig. Daher haben wir unsere Fachgebiete für Sie einzeln aufgegliedert.<br>Erfahren Sie mehr über uns und wählen Sie nun Ihre Wunschleistung aus.<br>Gerne beraten wir Sie vorab persönlich und helfen Ihnen eine maßgeschneiderte Dienstleistung für Sie zu finden.</p><div class="btn">Kontaktieren Sie uns</div></div>
  <footer class="ft"><div class="ft-addr"><p>Anschrift:<br>Kaltwacht Sicherheitsdienst Nürnberg e. K.<br>Lindenhofstr. 18<br>90471 Nürnberg</p><p>E-Mail:<br>info@kaltwacht-sicherheit.de</p><p>Telefon:<br>0800 / 555 010 0 (kostenfrei, 24h)<br>0911 / 555 012 30</p></div><div class="ft-links"><p>Impressum</p><p>Datenschutz</p><p>Anfahrt</p><p>Folgen Sie uns auf</p><div class="social"><i></i><i></i></div></div><p class="ft-copy">© Copyright 2020 Kaltwacht Sicherheitsdienst Nürnberg</p></footer>
</section>

<section class="page home" style="left:724px;top:552px;transform:scale(.5885)">
  <div class="photo hero ph-guard" role="img" aria-label="Einsatzleiter von hinten vor einer Kirche unter blauem Himmel"></div>
  <nav class="nav nav--light"><div class="logo"><i></i><span>KALTWACHT</span></div><div class="nav-links"><span class="is-active" style="border-color:var(--white)">Home</span><span>Leistungen</span><span>News</span><span>Unternehmen</span><span>Karriere</span><span class="cta">Kontakt</span></div></nav>
  <div class="side-social"><i></i><i></i></div>
  <span class="hero-arrow" style="left:40px">‹</span><span class="hero-arrow" style="right:40px">›</span>
  <div class="hero-copy" style="left:38px;top:112px"><h1 style="font-size:17px">… wir handeln in Ihrem Sinne</h1></div>
  <div class="hero-dots"><i></i><i></i><i></i></div>
  <div class="tabs"><span>Sicherheitsdienst</span><span>Detektei</span><span>Service</span><span>Schulungen</span></div>
  <div class="tiles">
    <div class="tile ph-tile1" role="img" aria-label="Sicherheitsmitarbeiter mit Helm"><span class="tile-arrow">›</span></div>
    <div class="tile ph-tile2" role="img" aria-label="Detektiv mit Fernglas im Auto"><span class="tile-arrow">›</span></div>
    <div class="tile ph-tile3" role="img" aria-label="Servicemitarbeiterin am Empfang"><span class="tile-arrow">›</span></div>
    <div class="tile ph-tile4" role="img" aria-label="Schulung im Besprechungsraum"><span class="tile-arrow">›</span></div>
  </div>
  <div class="photo about-photo ph-ceo" role="img" aria-label="Geschäftsführer im Anzug"></div>
  <div class="about"><h2>Über uns</h2><p>Wir sind ein inhabergeführtes Unternehmen mit Verantwortungsbewusstsein für Sicherheit und Service. Durch unseren eigenen hohen Qualitätsanspruch und unsere Flexibilität haben wir seit Firmengründung ein kontinuierliches Wachstum zu verzeichnen.</p><span class="more">›</span></div>
  <div class="help"><h2>Wie können wir Ihnen helfen…</h2><p>Unsere Leistungen sind vielfältig. Daher haben wir unsere Fachgebiete für Sie einzeln aufgegliedert.<br>Erfahren Sie mehr über uns und wählen Sie nun Ihre Wunschleistung aus.<br>Gerne beraten wir Sie vorab persönlich und helfen Ihnen eine maßgeschneiderte Dienstleistung für Sie zu finden.</p><div class="btn">Kontaktieren Sie uns</div></div>
  <footer class="ft"><div class="ft-addr"><p>Anschrift:<br>Kaltwacht Sicherheitsdienst Nürnberg e. K.<br>Lindenhofstr. 18<br>90471 Nürnberg</p><p>E-Mail:<br>info@kaltwacht-sicherheit.de</p><p>Telefon:<br>0800 / 555 010 0 (kostenfrei, 24h)<br>0911 / 555 012 30</p></div><div class="ft-links"><p>Impressum</p><p>Datenschutz</p><p>Anfahrt</p><p>Folgen Sie uns auf</p><div class="social"><i></i><i></i></div></div><p class="ft-copy">© Copyright 2020 Kaltwacht Sicherheitsdienst Nürnberg</p></footer>
</section>

</main>
</body>
</html>
```